Ad for regional magazine for startup "Varomek"

We need a small ad for a small German regional magazine for our startup company Varomek which provides on-premise service for all kind of electronic problems.

We also need the Indesign files to be able to make minor changes (e.g. the phone number) in the future.

An example ad that we used before (for another region with another phone number) is attached.

Industry/Entity Type

Technical Service

Requirements
Must have
• Needed contents:
• "Elektronik-Problem?" (Electronic problem?)
• "Ihr Media-Pannenhelfer kommt" (Your media helper comes)
• "TV, Video, Telefon, Smartphone, Internet, Computer"
• "Terminbuchung: 07051-3920648" (booking)
• "Soforthilfe - auch abends und am Wochenende" (immediate help - also in the evenings and at the weekend)
• "www.varomek.de"
• logo
• picture
• Size: 90mm (width) x 50-70mm (height)
• Font & colors: see attachment

```html
<!DOCTYPE html>
<html lang="de">
<head>
<meta charset="utf-8">
<title>Varomek Anzeige – Entwürfe</title>
<link href="https://fonts.googleapis.com/css2?family=Open+Sans:wght@400;600;700&display=swap" rel="stylesheet">
<style>
:root{
  --page:#ffffff;
  --frame:#9a9a9a;
  --caption:#8a8a8a;
  --ink:#222222;
  --slate:#4c4f54;
  --slate-light:#8c8e91;
  --lime:#c7dc3c;
  --green:#6fb43f;
  --teal:#38b5c6;
  --yellow:#f2bd2a;
  --navy:#1f4f7d;
  --grey-icon:#6a6d71;
  --orange:#ef5a2a;
  --leaf:#8cc43f;
  --logo-ink:#3c3f44;
  --white:#ffffff;
}
*{margin:0;padding:0;box-sizing:border-box}
html,body{width:1200px;height:521px;overflow:hidden;background:var(--page)}
.sheet{position:relative;width:1200px;height:521px;border:1px solid var(--frame);font-family:"Open Sans",Arial,sans-serif}
.option{position:absolute;top:25px;width:548px}
.option--one{left:28px}
.option--two{left:621px}
.ad{display:block;width:548px;height:426px}
.ad text{font-family:"Open Sans",Arial,sans-serif;fill:var(--white)}
.ad .brand{fill:var(--logo-ink);font-weight:700;font-size:30px;letter-spacing:1px}
.caption{text-align:center;color:var(--caption);font-size:18px;margin-top:12px}
.label{text-align:center;color:var(--ink);font-size:21px;margin-top:6px}
</style>
</head>
<body>
<div class="sheet">

  <section class="option option--one">
    <svg class="ad" viewBox="0 0 548 426" xmlns="http://www.w3.org/2000/svg">
      <defs>
        <linearGradient id="photoTone1" x1="0" y1="0" x2="1" y2="1">
          <stop offset="0" stop-color="#e9e6e2"/><stop offset=".5" stop-color="#b9aea4"/><stop offset="1" stop-color="#d8c8b4"/>
        </linearGradient>
        <linearGradient id="slate1" x1="0" y1="0" x2="1" y2="1">
          <stop offset="0" stop-color="var(--slate)"/><stop offset="1" stop-color="var(--slate-light)"/>
        </linearGradient>
        <linearGradient id="swoosh1" x1="0" x2="1">
          <stop offset="0" stop-color="var(--lime)"/><stop offset="1" stop-color="var(--green)"/>
        </linearGradient>
      </defs>
      <rect class="photo" width="548" height="426" fill="url(#photoTone1)" role="img" aria-label="Foto: Servicetechniker erklärt einem älteren Kunden ein Tablet"/>
      <path class="swoosh" d="M0,92 C150,175 320,255 548,292 L548,330 C320,300 150,250 0,150 Z" fill="url(#swoosh1)"/>
      <path class="panel" d="M0,118 C150,215 320,290 548,318 L548,426 L0,426 Z" fill="url(#slate1)"/>
      <path class="logo-tab" d="M372,0 H548 V67 H392 Q372,67 372,47 Z" fill="var(--white)"/>
      <text class="brand" x="460" y="44" text-anchor="middle">varomek</text>

      <g class="icon tv"><circle cx="67" cy="130" r="28" fill="var(--teal)"/><rect x="54" y="120" width="26" height="18" rx="2" fill="none" stroke="#fff" stroke-width="3"/><path d="M60,114 L67,120 L74,114" stroke="#fff" stroke-width="2" fill="none"/></g>
      <g class="icon video"><circle cx="139" cy="187" r="28" fill="var(--yellow)"/><rect x="124" y="177" width="30" height="20" fill="none" stroke="#fff" stroke-width="3"/><path d="M136,182 L145,187 L136,192 Z" fill="#fff"/></g>
      <g class="icon phone"><circle cx="224" cy="235" r="28" fill="var(--navy)"/><path d="M210,230 Q224,218 238,230 L238,234 L232,234 L231,230 L217,230 L216,234 L210,234 Z" fill="#fff"/><rect x="214" y="236" width="20" height="12" rx="2" fill="#fff"/></g>
      <g class="icon smartphone"><circle cx="313" cy="272" r="28" fill="var(--grey-icon)"/><rect x="303" y="257" width="16" height="28" rx="2" fill="none" stroke="#fff" stroke-width="2.5"/><circle cx="322" cy="278" r="4" fill="#fff"/></g>
      <g class="icon antenna"><circle cx="400" cy="295" r="28" fill="var(--orange)"/><path d="M393,310 L400,288 L407,310 M396,302 H404" stroke="#fff" stroke-width="2.5" fill="none"/><path d="M390,282 Q386,288 390,294 M410,282 Q414,288 410,294" stroke="#fff" stroke-width="2" fill="none"/></g>
      <g class="icon computer"><circle cx="490" cy="315" r="28" fill="var(--leaf)"/><rect x="474" y="303" width="24" height="17" fill="none" stroke="#fff" stroke-width="2.5"/><rect x="501" y="302" width="6" height="22" fill="#fff"/><path d="M480,326 H494" stroke="#fff" stroke-width="2.5"/></g>

      <text x="22" y="270" font-size="26" font-weight="600">Elektronik</text>
      <text x="22" y="303" font-size="26" font-weight="600">Problem?</text>
      <text x="22" y="333" font-size="16">Ihr Media-Pannenhelfer kommt</text>
      <text x="24" y="364" font-size="18" font-weight="700">Terminbuchung:</text>
      <text x="24" y="390" font-size="18" font-weight="700">07051-3920648</text>
      <text x="24" y="415" font-size="18" font-weight="700">www.varomek.de</text>
      <text x="411" y="388" font-size="16" text-anchor="middle">Soforthilfe - auch abends</text>
      <text x="411" y="410" font-size="16" text-anchor="middle">und am Wochenende</text>
    </svg>
    <p class="caption">90mm (width) x 70 hight</p>
    <p class="label">option 1</p>
  </section>

  <section class="option option--two">
    <svg class="ad" viewBox="0 0 548 426" xmlns="http://www.w3.org/2000/svg">
      <defs>
        <linearGradient id="photoTone2" x1="0" y1="0" x2="1" y2="1">
          <stop offset="0" stop-color="#e9e6e2"/><stop offset=".5" stop-color="#b9aea4"/><stop offset="1" stop-color="#d8c8b4"/>
        </linearGradient>
        <linearGradient id="swoosh2" x1="0" x2="1">
          <stop offset="0" stop-color="var(--lime)"/><stop offset="1" stop-color="var(--green)"/>
        </linearGradient>
      </defs>
      <rect class="panel" width="548" height="426" fill="var(--slate)"/>
      <path class="swoosh" d="M0,0 H548 V245 C450,292 320,300 210,290 C90,278 0,220 0,120 Z" fill="url(#swoosh2)"/>
      <path class="photo" d="M22,0 H548 V180 C470,238 340,248 250,240 C120,228 38,150 22,0 Z" fill="url(#photoTone2)" role="img" aria-label="Foto: Servicetechniker erklärt einem älteren Kunden ein Tablet"/>
      <path class="logo-tab" d="M345,0 H528 V46 Q528,66 508,66 H345 Z" fill="var(--white)"/>
      <text class="brand" x="436" y="43" text-anchor="middle">varomek</text>

      <g class="icon tv"><circle cx="38" cy="95" r="28" fill="var(--teal)"/><rect x="25" y="85" width="26" height="18" rx="2" fill="none" stroke="#fff" stroke-width="3"/><path d="M31,79 L38,85 L45,79" stroke="#fff" stroke-width="2" fill="none"/></g>
      <g class="icon video"><circle cx="100" cy="168" r="28" fill="var(--yellow)"/><rect x="85" y="158" width="30" height="20" fill="none" stroke="#fff" stroke-width="3"/><path d="M97,163 L106,168 L97,173 Z" fill="#fff"/></g>
      <g class="icon phone"><circle cx="182" cy="215" r="28" fill="var(--navy)"/><path d="M168,210 Q182,198 196,210 L196,214 L190,214 L189,210 L175,210 L174,214 L168,214 Z" fill="#fff"/><rect x="172" y="216" width="20" height="12" rx="2" fill="#fff"/></g>
      <g class="icon smartphone"><circle cx="281" cy="243" r="28" fill="var(--grey-icon)"/><rect x="271" y="228" width="16" height="28" rx="2" fill="none" stroke="#fff" stroke-width="2.5"/><circle cx="290" cy="249" r="4" fill="#fff"/></g>
      <g class="icon antenna"><circle cx="394" cy="233" r="28" fill="var(--orange)"/><path d="M387,248 L394,226 L401,248 M390,240 H398" stroke="#fff" stroke-width="2.5" fill="none"/><path d="M384,220 Q380,226 384,232 M404,220 Q408,226 404,232" stroke="#fff" stroke-width="2" fill="none"/></g>
      <g class="icon computer"><circle cx="479" cy="180" r="28" fill="var(--leaf)"/><rect x="463" y="168" width="24" height="17" fill="none" stroke="#fff" stroke-width="2.5"/><rect x="490" y="167" width="6" height="22" fill="#fff"/><path d="M469,191 H483" stroke="#fff" stroke-width="2.5"/></g>

      <text x="274" y="335" font-size="35" font-weight="600" text-anchor="middle">Elektronik Problem?</text>
      <text x="274" y="358" font-size="16" text-anchor="middle">Ihr Media-Pannenhelfer kommt</text>
      <text x="274" y="382" font-size="16" text-anchor="middle">Soforthilfe - auch abends und am Wochenende</text>
      <text x="274" y="411" font-size="19" font-weight="700" text-anchor="middle">Terminbuchung: 07051-3920648 | www.varomek.de</text>
    </svg>
    <p class="caption">90mm (width) x 70 hight</p>
    <p class="label">option 2</p>
  </section>

</div>
</body>
</html>
```